Ravel Trade Parts consulting and education services needs ClipNook channel with video intro

Well, www.raveltradeparts.example we think we have a nice Logo already but need to integrate it for a pleasing, simple. classy, all business signaling ClipNook account/channel were we are going to provide free consulting on the most common problem areas of ERP integration within the ERP system it self between the different functional modules and integration between other external systems, api webservices, digital collaboration and cloud solutions. Like exchange rates, deal grove, Orvano market place. Conceptual design and strategy level discussions on design and how to execute the implementation etc. Smallest technical tricks to history of systems and future predictions trying to help business users to navigate a more and more complex back office environment. We are using our +25 years of experience making it possible for you to challenge the IT department without having to hire a big five consulting firm. We want you to arm yourself just watching our ClipNook channel!

Target Market(s)

People working in large organizations using ERP systems - business users

Industry/Entity Type

Consulting and education providing knowledge about sytesm and integration

Colors
0054AA
0677BA
7BADD7
CADEEF
E8F1F8

Requirements
Must have
• Clean look using our existing logo
Nice to have
• message that anybody watching our videos will be able to challenge the IT department and consultants
Should not have
• Any other or new logo, many colors and not only logo should also show a message

```html
<!DOCTYPE html>
<html lang="en">
<head>
<meta charset="utf-8">
<title>Ravel Trade Parts – Connected ERP for Anybody</title>
<link rel="stylesheet" href="https://fonts.googleapis.com/css2?family=Kanit:wght@500;600&family=Roboto+Condensed:wght@700&display=swap">
<style>
  :root {
    --navy: #0b1470;
    --brand-deep: #0054AA;
    --brand-mid: #0677BA;
    --brand-light: #7BADD7;
    --brand-pale: #CADEEF;
    --brand-mist: #E8F1F8;
    --cyan: #00b8f2;
    --white: #ffffff;
    --hex-line: rgba(255,255,255,0.92);
  }
  html, body {
    margin: 0;
    padding: 0;
    width: 1200px;
    height: 675px;
    overflow: hidden;
    background: #000;
  }
  .canvas {
    position: relative;
    width: 1200px;
    height: 675px;
    overflow: hidden;
  }
  .backdrop {
    position: absolute;
    inset: 0;
    background:
      radial-gradient(ellipse 420px 260px at 470px 160px, rgba(240,215,170,0.55), transparent 70%),
      radial-gradient(ellipse 380px 420px at 1020px 500px, rgba(14,26,60,0.95), transparent 75%),
      linear-gradient(90deg, #5e4c38 0%, #8f7658 22%, #b99c77 45%, #8d7a63 62%, #2a3350 78%, #141c36 100%);
  }
  .headline {
    position: absolute;
    top: 50px;
    left: 0;
    width: 1200px;
    margin: 0;
    text-align: center;
    white-space: nowrap;
    font-family: "Roboto Condensed", "Arial Narrow", sans-serif;
    font-weight: 700;
    font-size: 54px;
    line-height: 1;
    letter-spacing: -0.6px;
    filter: drop-shadow(0 0 5px rgba(255,232,160,0.75));
  }
  .headline span {
    background: linear-gradient(90deg, var(--navy) 0%, #0c2a9a 28%, #0a63d8 48%, var(--cyan) 70%, #0a58e0 82%, var(--navy) 100%);
    -webkit-background-clip: text;
    background-clip: text;
    color: transparent;
  }
  .headline .small-word {
    font-size: 26px;
    vertical-align: 22px;
    margin: 0 4px;
  }
  .module-map {
    position: absolute;
    inset: 0;
  }
  .hex-cell { fill: rgba(10,14,30,0.10); stroke: var(--hex-line); stroke-width: 0.9; }
  .hex-label {
    font-family: "Kanit", sans-serif;
    font-weight: 500;
    font-size: 23px;
    fill: var(--white);
    text-anchor: middle;
  }
  .hex-erp {
    font-family: "Kanit", sans-serif;
    font-weight: 500;
    font-size: 66px;
    fill: var(--white);
    text-anchor: middle;
  }
  .hex-dollar {
    font-family: "Kanit", sans-serif;
    font-weight: 600;
    font-size: 100px;
    fill: var(--white);
    text-anchor: middle;
  }
  .icon { fill: var(--white); }
  .brand-panel {
    position: absolute;
    left: 0;
    top: 518px;
    width: 357px;
    height: 144px;
    background: var(--white);
    border-radius: 0 72px 72px 0;
  }
  .brand-mark {
    position: absolute;
    left: 140px;
    top: 14px;
    width: 50px;
    height: 50px;
    border-radius: 50%;
    background: var(--brand-deep);
  }
  .brand-name {
    position: absolute;
    left: 0;
    top: 76px;
    width: 330px;
    margin: 0;
    text-align: center;
    font-family: "Kanit", sans-serif;
    font-weight: 600;
    font-size: 31px;
    line-height: 1;
    color: var(--brand-deep);
  }
</style>
</head>
<body>
<main class="canvas">
  <div class="backdrop" role="img" aria-label="Blurred photo of a businessman in a dark suit pointing at the screen, in a warmly lit office hall"></div>

  <h1 class="headline"><span>Connected Enterprise Resource Planning</span><span class="small-word">for</span><span>Anybody</span></h1>

  <svg class="module-map" width="1200" height="675" viewBox="0 0 1200 675" aria-label="ERP modules">
    <defs>
      <polygon id="hex" points="-85,0 -42.5,-73.6 42.5,-73.6 85,0 42.5,73.6 -42.5,73.6"/>
      <linearGradient id="erp-fill" x1="0" y1="0" x2="1" y2="1">
        <stop offset="0" stop-color="#47c2f2"/>
        <stop offset="0.5" stop-color="#1679d2"/>
        <stop offset="1" stop-color="#0a2f9e"/>
      </linearGradient>
    </defs>

    <!-- hex grid -->
    <g class="hex-grid">
      <use href="#hex" class="hex-cell" x="99.4" y="312.2"/>
      <use href="#hex" class="hex-cell" x="239.5" y="233.4"/>
      <use href="#hex" class="hex-cell" x="240.9" y="397"/>
      <use href="#hex" class="hex-cell" x="383.9" y="305.6"/>
      <use href="#hex" class="hex-cell" x="383" y="482.3"/>
      <use href="#hex" class="hex-cell" x="527.3" y="226.4"/>
      <use href="#hex" class="hex-cell" x="527.3" y="386.3"/>
      <use href="#hex" class="hex-cell" x="672.7" y="300"/>
      <use href="#hex" class="hex-cell" x="673.6" y="468.8"/>
      <use href="#hex" class="hex-cell" x="812.3" y="225"/>
      <use href="#hex" class="hex-cell" x="814.2" y="386.3"/>
      <use href="#hex" class="hex-cell" x="955.3" y="305.6"/>
      <use href="#hex" class="hex-cell" x="957.7" y="469.7"/>
      <use href="#hex" class="hex-cell" x="1100.6" y="387.2"/>
    </g>

    <!-- highlighted ERP cell -->
    <polygon points="-79,0 -39.5,-68.5 39.5,-68.5 79,0 39.5,68.5 -39.5,68.5" transform="translate(672.7 300)" fill="url(#erp-fill)"/>
    <text class="hex-erp" x="672.7" y="322">ERP</text>

    <!-- labels -->
    <text class="hex-label" x="99.4" y="320">inventory</text>
    <text class="hex-label" x="239.5" y="225">finance</text>
    <text class="hex-label" x="239.5" y="253">accounting</text>
    <text class="hex-label" x="383" y="488">sales</text>
    <text class="hex-label" x="673.6" y="474">service</text>
    <text class="hex-label" x="812.3" y="230">delivery</text>
    <text class="hex-label" x="957.7" y="461">human</text>
    <text class="hex-label" x="957.7" y="489">resources</text>
    <text class="hex-label" x="1100.6" y="395">CMR</text>
    <text class="hex-label" x="527.3" y="222">Ravel</text>
    <text class="hex-label" x="527.3" y="249">Trade Parts</text>

    <!-- dollar icon -->
    <text class="hex-dollar" x="383.9" y="340">$</text>

    <!-- document icon -->
    <g class="doc-icon" transform="translate(194 354)">
      <rect class="icon" x="0" y="0" width="4" height="98"/>
      <rect class="icon" x="0" y="94" width="74" height="4"/>
      <rect class="icon" x="8" y="0" width="83" height="90"/>
      <g stroke="#8a7a66" stroke-width="1.6">
        <line x1="21" y1="18" x2="71" y2="18"/><line x1="21" y1="24" x2="71" y2="24"/>
        <line x1="21" y1="30" x2="71" y2="30"/><line x1="21" y1="36" x2="71" y2="36"/>
        <line x1="21" y1="42" x2="71" y2="42"/><line x1="21" y1="48" x2="71" y2="48"/>
        <line x1="21" y1="54" x2="71" y2="54"/><line x1="21" y1="60" x2="71" y2="60"/>
        <line x1="21" y1="66" x2="71" y2="66"/><line x1="21" y1="72" x2="71" y2="72"/>
      </g>
    </g>

    <!-- factory icon -->
    <g class="factory-icon" transform="translate(491 354)">
      <path class="icon" d="M0 6 H13 V20 H27 V46 L40 34 V50 L53 38 V0 H58 V38 L67 50 L80 38 V74 H0 Z"/>
      <rect x="7" y="17" width="5" height="5" fill="#6d5c48"/><rect x="13" y="17" width="5" height="5" fill="#6d5c48"/>
      <rect x="7" y="23" width="5" height="5" fill="#6d5c48"/><rect x="13" y="23" width="5" height="5" fill="#6d5c48"/>
      <circle cx="35" cy="56" r="3.4" fill="#6d5c48"/><circle cx="53" cy="56" r="3.4" fill="#6d5c48"/><circle cx="71" cy="56" r="3.4" fill="#6d5c48"/>
      <path d="M52 -6 q-4 -5 1 -10 M56 -6 q-4 -5 1 -10" stroke="#fff" stroke-width="1" fill="none"/>
    </g>

    <!-- gears icon -->
    <g class="gears-icon" fill="none" stroke="#fff">
      <circle cx="780" cy="389" r="18" stroke-width="13"/>
      <circle cx="780" cy="389" r="26" stroke-width="7" stroke-dasharray="6 7"/>
      <circle cx="818" cy="362" r="11" stroke-width="8"/>
      <circle cx="818" cy="362" r="17" stroke-width="5" stroke-dasharray="4 5"/>
      <circle cx="835" cy="410" r="18" stroke-width="13"/>
      <circle cx="835" cy="410" r="26" stroke-width="7" stroke-dasharray="6 7"/>
    </g>

    <!-- truck icon -->
    <g class="truck-icon" transform="translate(908 281)">
      <path class="icon" d="M1 0 H59 V57 H0 Z"/>
      <path class="icon" d="M63 15 H85 L100 42 V57 H63 Z"/>
      <path d="M69 20 H82 L92 38 H69 Z" fill="#1c2748"/>
      <circle cx="14" cy="59" r="5" fill="#1c2748" stroke="#fff" stroke-width="2"/>
      <circle cx="27" cy="59" r="5" fill="#1c2748" stroke="#fff" stroke-width="2"/>
      <circle cx="86" cy="59" r="5" fill="#1c2748" stroke="#fff" stroke-width="2"/>
    </g>
  </svg>

  <div class="brand-panel">
    <span class="brand-mark"></span>
    <p class="brand-name">Ravel Trade Parts</p>
  </div>
</main>
</body>
</html>
```